Looking for Landingpage / Website Designer

We are looking for a Web Designer / Developer for our upcoming Start Up Websites. The first project will be a simple responsive business website with a CTA- Button and an optional Newsletter Opt-In. We do aim for a modern online business approach, since we are a young company.

It is necessary to understand, that we need a conversion orientated design, not a wordpress blog with widgets and galleries.

We are currently discussing how it is going to happen and what preferences we need to focus on.

What we know is, that it should be more of a landing page with an option of adding 2 or 3 Navigation points.

We even thought about using services like plumvesta.com or crintofold.com to have an easier approach for future customizations and A/B testing.

We'd love to see how you fit the design/colors to the upcoming logo
(which is not the final version yet )

hope you can do something about that.

For the Structure.

1. Bracket

Slogan plus a preview text of what we are offering. On the right side a video placeholder plus CTA button.

2. Bracket

Illustrating 3 Benefits. On the right side - Opt in for Contact/Newsletter and CTA Button

3. Bracket

Picture with text just like you have it with the testimonial

You can orientate yourself towards to that landing page example as well:

http://cdn2.zorvellink.net/hub/53/file-581676469-png/Blog-Related_Images/plumvesta_landing_page.png?t=1416543075530

If our collaboration is going well, we would like to stay in touch for further projects.
Updates

Reason: There are 3 Design we do really like but, don't fit exactly our needs. 5 Days max.

Reason: For final adjustments.

I just uploaded the final logo :) Thank you for your commitment so far!

Target Market(s)

Our targeted audience could be almost everybody, who looks for an average paid side job (students, unemployed, house wives and whatever you can imagine). Maybe this is enough information for you to get a mere perception of what this is all about.

Industry/Entity Type

Business

Coding

Coded - Design and coding required

Font styles to use
Serif
Sans Serif

Colors
acd037
5c5c5c
33a6d7

Requirements
Must have
• Registration Opt-In
Responsive on any Device
Customizable
A benefits navigation just like in that example I've uploaded.
Nice to have
• As fast as possible ;D

```html
<!DOCTYPE html>
<html lang="en">
<head>
<meta charset="utf-8">
<title>Workvanta.de</title>
<link href="https://fonts.googleapis.com/css2?family=Lato:ital,wght@0,400;0,700;1,700&display=swap" rel="stylesheet">
<style>
:root{
  --dark:#3f3735;
  --green:#4fb848;
  --olive:#7b7a6c;
  --white:#ffffff;
  --ink:#3f3735;
  --muted:#4a4442;
  --field-text:#7b7a6c;
  --hero-light:#fafafa;
  --hero-mid:#e9e8e6;
}
*{box-sizing:border-box;margin:0;padding:0}
html,body{width:1005px;height:1200px;overflow:hidden;background:var(--white)}
body{font-family:'Lato',sans-serif;position:relative;color:var(--ink)}
.site-header{position:absolute;left:0;top:0;width:1005px;height:84px;background:var(--dark)}
.brand{position:absolute;left:125px;top:14px;display:flex;align-items:center;gap:10px}
.brand-dot{width:56px;height:56px;border-radius:50%;background:var(--green)}
.brand-name{font-size:42px;font-weight:700;color:var(--green);letter-spacing:-0.5px}
.main-nav{position:absolute;left:522px;top:0;height:84px;display:flex}
.main-nav a{display:block;height:84px;line-height:79px;color:var(--white);font-size:13.5px;font-weight:700;text-decoration:none}
.main-nav a.is-active{background:var(--green);padding:0 7px}
.main-nav a:not(.is-active){padding:0 7.5px}
.hero{position:absolute;left:0;top:84px;width:1005px;height:379px;
  background:linear-gradient(90deg,var(--hero-light) 0%,var(--hero-mid) 50%,var(--hero-light) 100%)}
.hero-arrow{position:absolute;top:173px;width:35px;height:35px;background:var(--dark);display:flex;align-items:center;justify-content:center}
.hero-arrow.prev{left:0}
.hero-arrow.next{right:0}
.welcome{position:absolute;left:0;top:463px;width:1005px;height:265px;background:var(--dark)}
.accent-bar{position:absolute;width:7px;background:var(--green)}
.welcome .accent-bar{left:144px;top:28px;height:203px}
.welcome h1{position:absolute;left:178px;top:20px;font-size:29.5px;font-weight:700;color:var(--white)}
.welcome .intro{position:absolute;left:179px;top:62px;width:346px;font-size:13.2px;line-height:20.4px;color:var(--white);text-align:justify}
.signup{position:absolute;left:652px;top:16px;width:217px;height:231px;background:var(--olive);border-radius:3px}
.signup h2{text-align:center;font-size:15px;font-weight:700;color:var(--white);margin-top:11px}
.signup .field{position:absolute;left:17px;width:184px;height:27px;background:var(--white);border-radius:3px;font-size:11.5px;font-style:italic;font-weight:700;color:var(--field-text);padding:7px 0 0 21px}
.signup .submit{position:absolute;left:68px;top:190px;width:85px;height:27px;background:var(--green);border-radius:2px;color:var(--white);font-size:13.5px;font-style:italic;font-weight:700;text-align:center;line-height:27px}
.mission{position:absolute;left:0;top:728px;width:1005px;height:249px;background:var(--white)}
.mission .accent-bar{left:144px;top:21px;height:187px}
.mission h2{position:absolute;left:178px;top:14px;font-size:30px;font-weight:700;color:var(--ink)}
.mission .lead{position:absolute;left:182px;top:60px;width:246px;font-size:11.6px;line-height:20.4px;color:var(--muted);text-align:justify}
.benefit{position:absolute;top:28px;width:130px;text-align:center}
.benefit svg{display:block;margin:0 auto;height:44px}
.benefit p{margin-top:19px;font-size:10px;line-height:13.3px;color:var(--ink)}
.benefit .more{display:block;margin-top:11px;font-size:13px;font-style:italic;font-weight:700;color:var(--ink)}
.testimonial{position:absolute;left:0;top:977px;width:1005px;height:181px;background:var(--olive)}
.testimonial .accent-bar{left:144px;top:16px;height:152px}
.avatar{position:absolute;left:189px;top:43px;width:85px;height:85px;border-radius:50%;border:3px solid var(--dark);background:radial-gradient(circle at 50% 40%,#c9ccd0,#8a8f98)}
.quote-mark{position:absolute;font-family:'Georgia',serif;font-size:40px;font-weight:700;color:var(--white);line-height:1}
.quote-open{left:310px;top:33px}
.quote-close{left:848px;top:88px}
.testimonial blockquote{position:absolute;left:346px;top:57px;width:472px;text-align:center;font-size:10.6px;line-height:13.5px;color:var(--white)}
.testimonial cite{position:absolute;left:346px;top:114px;width:368px;text-align:center;font-style:normal;font-size:13.2px;font-weight:700;color:var(--white)}
.site-footer{position:absolute;left:0;top:1158px;width:1005px;height:42px;background:var(--dark);text-align:center;line-height:42px;color:var(--white);font-size:13px;font-style:italic;font-weight:700}
</style>
</head>
<body>
<header class="site-header">
  <div class="brand"><span class="brand-dot"></span><span class="brand-name">Workvanta.de</span></div>
  <nav class="main-nav">
    <a class="is-active" href="#">Home</a>
    <a href="#">About Us</a>
    <a href="#">Services</a>
    <a href="#">Testimonial</a>
    <a href="#">Contact Us</a>
  </nav>
</header>

<section class="hero" role="img" aria-label="Hero photo: businessman in a suit with a light bulb for a head, in front of hand-drawn business sketches">
  <div class="hero-arrow prev"><svg width="14" height="12" viewBox="0 0 14 12"><path d="M7 1L2 6l5 5M12 1L7 6l5 5" fill="none" stroke="#4fb848" stroke-width="1.6"/></svg></div>
  <div class="hero-arrow next"><svg width="14" height="12" viewBox="0 0 14 12"><path d="M2 1l5 5-5 5M7 1l5 5-5 5" fill="none" stroke="#4fb848" stroke-width="1.6"/></svg></div>
</section>

<section class="welcome">
  <span class="accent-bar"></span>
  <h1>Welcome To Workvanta.de</h1>
  <p class="intro">Lorem Ipsum is simply dummy text of the printing and typesetting industry. Lorem Ipsum has been the industry's standard dummy text ever since the 1500s, when an unknown printer took a galley of type and scrambled it to make a type specimen book.<br>Lorem Ipsum is simply dummy text of the printing and typesetting industry.&nbsp; took a galley of type and scrambled it to make a type specimen book.</p>
  <form class="signup">
    <h2>Free Consultion Signup</h2>
    <div class="field" style="top:47px">Your Name</div>
    <div class="field" style="top:81px">Email Address</div>
    <div class="field" style="top:114px">Company Name</div>
    <div class="field" style="top:149px">Phone</div>
    <div class="submit">Submit</div>
  </form>
</section>

<section class="mission">
  <span class="accent-bar"></span>
  <h2>Our Mission</h2>
  <p class="lead">Lorem Ipsum is simply dummy text of the printing and typesetting industry. Lorem Ipsum has been the industry's standard dummy text ever since the 1500s, when an unknown printer took a galley of type and scrambled it to make a type specimen book.</p>

  <div class="benefit" style="left:438px">
    <svg viewBox="0 0 44 44" width="44"><g fill="none" stroke="#4fb848" stroke-width="5" stroke-linejoin="round"><path d="M14 18l8-13 6 10"/><path d="M32 22l7 12H26"/><path d="M18 36H5l6-11"/></g><g fill="#4fb848"><path d="M24 17l8-4-1 9z"/><path d="M26 30l-3 6 3 6z"/><path d="M7 22l8 2-6 6z"/></g></svg>
    <p>Dummy text of the printing and typesetting industry. Lorem Ipsum has been the industry's standard dummy text ever since the 1500s,</p>
    <span class="more">Read More</span>
  </div>
  <div class="benefit" style="left:587px">
    <svg viewBox="0 0 44 44" width="44"><path d="M13 20v-8a7 7 0 0 1 14 0v2" fill="none" stroke="#4fb848" stroke-width="5"/><rect x="8" y="20" width="28" height="20" rx="2" fill="#4fb848"/></svg>
    <p>Dummy text of the printing and typesetting industry. Lorem Ipsum has been the industry's standard dummy text ever since the 1500s,</p>
    <span class="more">Read More</span>
  </div>
  <div class="benefit" style="left:743px">
    <svg viewBox="0 0 50 44" width="50"><g fill="#4fb848"><circle cx="25" cy="11" r="8"/><circle cx="11" cy="14" r="6"/><circle cx="39" cy="14" r="6"/><path d="M12 44v-9a13 13 0 0 1 26 0v9z"/><path d="M0 36v-4a9 9 0 0 1 13-8 16 16 0 0 0-4 12z"/><path d="M50 36v-4a9 9 0 0 0-13-8 16 16 0 0 1 4 12z"/></g></svg>
    <p>Dummy text of the printing and typesetting industry. Lorem Ipsum has been the industry's standard dummy text ever since the 1500s,</p>
    <span class="more">Read More</span>
  </div>
</section>

<section class="testimonial">
  <span class="accent-bar"></span>
  <div class="avatar" role="img" aria-label="Portrait photo of the company director"></div>
  <span class="quote-mark quote-open">&ldquo;</span>
  <blockquote>When an unknown printer took a galley of type and scrambled it to make a type specimen book. It has survived not only five centuries, but also the leap into electronic typesetting</blockquote>
  <span class="quote-mark quote-close">&rdquo;</span>
  <cite>Teodor Vassly - Director Of Company Name</cite>
</section>

<footer class="site-footer">Built Using the Plumvesta Landing Page</footer>
</body>
</html>
```